Zielgruppe
Wir verkaufen spezielle Teemischungen an Frauen, die schwanger werden möchten und sich gezielt ein Mädchen oder einen Jungen wünschen. Die Rezeptur unseres Tees, ist speziell auf den jeweiligen Wunsch abgestimmt. Wir verkaufen daher einen Sonnenwiese Tee und einen Bergquelle Tee.
Aufgabenstellung
Wir benötigen ein Etikett Design für den Sonnenwiese Tee. Wenn das Etikett fertig designed wurde, würden wir gerne anschließend ein Etikett für den Bergquelle Tee designen lassen. Das Design sollte klar, hochwertig und modern wirken. Es sollte erkennbar sein, dass der Tee speziell für Frauen mit einem Mädchenwunsch ist. Die Hintergrundfarbe des Designes bzw. des Etiketts sollte in zart rosa sein.

```html
<!DOCTYPE html>
<html lang="de">
<head>
<meta charset="utf-8">
<title>Sonnenwiese Tee – Etikett</title>
<link href="https://fonts.googleapis.com/css2?family=Advent+Pro:wght@200;300;400&display=swap" rel="stylesheet">
<style>
  :root {
    --backdrop: #f3e4c8;
    --blush: #e087a2;
    --blush-deep: #d37f97;
    --paper: #ecebe9;
    --paper-shade: #e2e1df;
    --ink: #262626;
    --accent: #c87590;
    --rule: rgba(255, 255, 255, 0.75);
    --illustration: #d6d4d1;
  }
  * { margin: 0; padding: 0; box-sizing: border-box; }
  html, body {
    width: 1200px;
    height: 900px;
    overflow: hidden;
    background: var(--backdrop);
    font-family: "Advent Pro", sans-serif;
    color: var(--ink);
  }
  .label {
    position: absolute;
    left: 335px;
    top: 20px;
    width: 530px;
    height: 860px;
    overflow: hidden;
    background: linear-gradient(180deg, var(--paper) 0%, var(--paper-shade) 100%);
  }
  .label__blush {
    position: absolute;
    left: 0; top: 0;
    width: 266px;
    height: 100%;
    background: linear-gradient(180deg, var(--blush-deep) 0%, var(--blush) 45%, var(--blush-deep) 100%);
  }
  .brand-seal {
    position: absolute;
    left: 190px;
    top: 72px;
    width: 184px;
    height: 184px;
    border-radius: 50%;
    background: var(--paper);
    display: flex;
    align-items: center;
    justify-content: center;
  }
  .brand-seal__name {
    font-size: 40px;
    font-weight: 300;
    letter-spacing: 2px;
    color: var(--accent);
  }
  .product-title {
    position: absolute;
    left: 30px;
    top: 292px;
    font-size: 59px;
    font-weight: 300;
    letter-spacing: 0.5px;
    line-height: 1;
    white-space: nowrap;
  }
  .claim {
    position: absolute;
    left: 55px;
    top: 418px;
    font-size: 25px;
    font-weight: 300;
    line-height: 28px;
  }
  .divider {
    position: absolute;
    left: 55px;
    width: 211px;
    height: 1px;
    background: var(--rule);
  }
  .divider--first { top: 505px; }
  .divider--second { top: 577px; }
  .endorsement {
    position: absolute;
    left: 57px;
    top: 529px;
    font-size: 25px;
    font-weight: 300;
    white-space: nowrap;
  }
  .benefits {
    position: absolute;
    left: 57px;
    top: 591px;
    list-style: none;
    font-size: 19px;
    font-weight: 300;
    line-height: 21px;
  }
  .benefits li {
    display: flex;
    align-items: center;
    gap: 8px;
    white-space: nowrap;
  }
  .benefits li::before {
    content: "";
    width: 13px;
    height: 13px;
    border-radius: 50%;
    background: var(--ink);
    flex: none;
  }
  .illustration-slot {
    position: absolute;
    left: 348px;
    top: 357px;
    width: 122px;
    height: 350px;
    border-radius: 50px 50px 6px 6px;
    background: linear-gradient(180deg, var(--illustration) 0%, var(--paper-shade) 100%);
  }
  .tagline {
    position: absolute;
    right: 70px;
    top: 746px;
    font-size: 37px;
    font-weight: 300;
    white-space: nowrap;
  }
  .tagline__accent { color: var(--accent); }
</style>
</head>
<body>
  <main class="label">
    <div class="label__blush"></div>

    <div class="brand-seal">
      <span class="brand-seal__name">Lunavie</span>
    </div>

    <h1 class="product-title">SONNENWIESETEE</h1>

    <p class="claim">außergewöhnliche<br>Kinderwunsch<br>Rezeptur</p>
    <div class="divider divider--first"></div>
    <p class="endorsement">von Müttern empfohlen</p>
    <div class="divider divider--second"></div>

    <ul class="benefits">
      <li>100% natürlich</li>
      <li>aus kontrolliertem Anbau</li>
      <li>Premium Qualität</li>
      <li>enthält Matcha</li>
      <li>inklusive E-Book!</li>
    </ul>

    <div class="illustration-slot" role="img" aria-label="Strichzeichnung einer schwangeren Frau mit Blumenkranz im langen Kleid, die Hände am Bauch"></div>

    <p class="tagline">natürlich <span class="tagline__accent">beeinflussen</span></p>
  </main>
</body>
</html>
```